Cocktail-Making Assistant App re-design

Ok boys and girls, here's the deal:
I have an android app which is almost complete, but needs a design overhaul.

The app is a standard cocktail-making assistant: gives you a list of cocktails and the ability to see which cocktail you can make out of those ingredients (drinks, fruit, etc) you have at home.

I've attached some general app flow, as well as detailed requirements/explanation presentation. Most of those things are just FYI, so that you know what it's about.

3 screens are the most important (main screen, cocktail view screen, ingredient view screen), meaning I will pick the design mostly based on ideas for those 3 things, with the fourth being a rather simple list (given on attached flow, third tier)
Some other screens are derived from that, with some minor changes on it, but you shouldn't care about that.

There are lots of other, non-explained things which I said nothing about only because they are (from design point of view) completely the same and would only make it seem more complicated.

I don't want to influence the colour scheme, but the app will be released under RedFern developer name (having a light colured red fern as a logo) so I suppose some brownish design, for example, will not really fit nicely. If you, however, have a killer which you are confident will prove me wrong, I'm looking forward to seeing it!

It should be a serious, elegant look (as opposed to cartoonish, but we are not aiming for a business look at all!), not cluttered with details, no clubbing themes, glitter and so on.

Test apk file available on request (Android 2.3+).

Edit: payment is now guaranteed
Also please note that currently, the favorite, "heart" button has a motion effect:
on click it flies out of the screen to the left (white heart) and comes back to the screen as a red heart. Take that into consideration, if it means anything to you.
Updates

Target Market(s)

Whoever you imagine would enjoy drinking cocktails

Industry/Entity Type

Business

Requirements
Must have
• Everything is said in the provided documentation - images say more than I could possibly write here.
Nice to have
• As said, most of the icons are a nice-to-have. Only those which are critically linked to the rest of the design must be provided. More details in the docs.
Should not have
• No cartoon look, No zillion colours

```html
<!DOCTYPE html>
<html lang="en">
<head>
<meta charset="utf-8">
<title>Cocktail Search</title>
<link rel="stylesheet" href="https://fonts.googleapis.com/css2?family=Roboto:wght@300;400;500;700&display=swap">
<style>
  :root {
    --page-bg: #e8edf0;
    --header-bg: #86e2f8;
    --back-bg: #5fcdee;
    --back-arrow: #1f7fa6;
    --title-strong: #1c4f68;
    --title-soft: #2f86ac;
    --screen-top: #79c7dd;
    --screen-mid: #2c6b8e;
    --screen-bottom: #0b2440;
    --search-bg: #3c8fb3;
    --search-text: #9fe6fb;
    --search-btn: #2f6f94;
    --row-bg: #f3f4f5;
    --row-line: #e1e3e5;
    --name: #3d4246;
    --star: #0f5d9c;
    --star-empty: #9ea4a9;
    --meta: #8a9096;
    --count: #2d78b6;
    --tick: #4caf1f;
  }
  * { box-sizing: border-box; margin: 0; padding: 0; }
  html, body {
    width: 1000px; height: 1200px; overflow: hidden;
    background: var(--page-bg);
    font-family: "Roboto", sans-serif;
  }
  .screen {
    position: absolute; left: 50px; top: 0;
    width: 900px; height: 1200px; overflow: hidden;
    background: linear-gradient(180deg, var(--screen-top) 0%, var(--screen-mid) 55%, var(--screen-bottom) 100%);
  }
  .app-header {
    position: absolute; left: 0; top: 0; width: 900px; height: 131px;
    background: var(--header-bg);
  }
  .back-button {
    position: absolute; left: 0; top: 0; width: 150px; height: 131px;
    background: var(--back-bg);
    display: flex; align-items: center; justify-content: center;
  }
  .app-title {
    position: absolute; left: 0; right: 0; top: 0; height: 131px;
    display: flex; align-items: center; justify-content: center;
    font-weight: 300; font-size: 54px; letter-spacing: -0.5px;
    color: var(--title-strong); padding-left: 0;
  }
  .app-title .soft { color: var(--title-soft); margin-left: 12px; }

  .search-bar {
    position: absolute; left: 37px; top: 163px; width: 826px; height: 113px;
    background: var(--search-bg); border-radius: 6px;
    box-shadow: inset 0 1px 3px rgba(0,0,0,.18);
  }
  .search-placeholder {
    position: absolute; left: 52px; top: 0; height: 113px;
    display: flex; align-items: center;
    font-weight: 300; font-size: 37px; color: var(--search-text);
  }
  .search-button {
    position: absolute; right: 0; top: 0; width: 113px; height: 113px;
    background: var(--search-btn); border-radius: 0 6px 6px 0;
    display: flex; align-items: center; justify-content: center;
  }

  .cocktail-list {
    position: absolute; left: 37px; top: 298px; width: 826px; height: 827px;
    background: var(--row-bg); border-radius: 6px; overflow: hidden;
    box-shadow: 0 6px 18px rgba(0,0,0,.25);
  }
  .cocktail-row {
    position: relative; height: 150px;
    border-bottom: 2px solid var(--row-line);
  }
  .thumb {
    position: absolute; left: 19px; top: 19px; width: 131px; height: 112px;
    border-radius: 6px;
  }
  .thumb.bushwacker { background: linear-gradient(135deg, #b98a5a 0%, #d8c2a0 45%, #8a5a32 100%); }
  .thumb.belmont { background: radial-gradient(circle at 50% 50%, #c8232f 0%, #d95a60 30%, #ffffff 62%); }
  .thumb.shade { background: radial-gradient(circle at 50% 55%, #7a1422 0%, #3a1a18 45%, #1c1410 100%); }
  .cocktail-name {
    position: absolute; left: 187px; top: 22px;
    font-weight: 300; font-size: 45px; color: var(--name); white-space: nowrap;
  }
  .rating {
    position: absolute; left: 185px; top: 88px; display: flex; gap: 9px;
  }
  .rating svg { width: 42px; height: 42px; display: block; }
  .have {
    position: absolute; right: 36px; top: 94px;
    display: flex; align-items: center; gap: 10px;
    font-weight: 300; font-size: 26px; color: var(--meta); white-space: nowrap;
  }
  .have b { font-weight: 500; color: var(--count); }
  .have.complete .total { font-weight: 500; color: var(--count); }
  .list-fade {
    position: absolute; left: 0; right: 0; bottom: 0; height: 90px;
    background: linear-gradient(180deg, rgba(243,244,245,0) 0%, rgba(243,244,245,.92) 55%, var(--row-bg) 100%);
  }
</style>
</head>
<body>
<svg width="0" height="0" style="position:absolute">
  <defs>
    <symbol id="star-full" viewBox="0 0 24 24">
      <path d="M12 1.8l3 6.6 7.2.8-5.4 4.9 1.5 7.1L12 17.6l-6.3 3.6 1.5-7.1L1.8 9.2 9 8.4z" fill="var(--star)"/>
    </symbol>
    <symbol id="star-empty" viewBox="0 0 24 24">
      <path d="M12 1.8l3 6.6 7.2.8-5.4 4.9 1.5 7.1L12 17.6l-6.3 3.6 1.5-7.1L1.8 9.2 9 8.4z" fill="none" stroke="var(--star-empty)" stroke-width="1.1" stroke-linejoin="round"/>
    </symbol>
    <clipPath id="left-half"><rect x="0" y="0" width="12" height="24"/></clipPath>
    <symbol id="star-half" viewBox="0 0 24 24">
      <path d="M12 1.8l3 6.6 7.2.8-5.4 4.9 1.5 7.1L12 17.6l-6.3 3.6 1.5-7.1L1.8 9.2 9 8.4z" fill="none" stroke="var(--star-empty)" stroke-width="1.1" stroke-linejoin="round"/>
      <path d="M12 1.8l3 6.6 7.2.8-5.4 4.9 1.5 7.1L12 17.6l-6.3 3.6 1.5-7.1L1.8 9.2 9 8.4z" fill="var(--star)" clip-path="url(#left-half)"/>
    </symbol>
  </defs>
</svg>

<main class="screen">
  <header class="app-header">
    <div class="back-button">
      <svg width="56" height="48" viewBox="0 0 28 24" aria-label="Back">
        <path d="M12 3L3 12l9 9M3 12h22" fill="none" stroke="var(--back-arrow)" stroke-width="4.2" stroke-linecap="round" stroke-linejoin="round"/>
      </svg>
    </div>
    <h1 class="app-title">Cocktail<span class="soft">Search</span></h1>
  </header>

  <div class="search-bar">
    <span class="search-placeholder">Search All Categories</span>
    <div class="search-button">
      <svg width="56" height="56" viewBox="0 0 24 24" aria-label="Search">
        <circle cx="10" cy="10" r="6.5" fill="none" stroke="#ffffff" stroke-width="2.6"/>
        <path d="M15 15l5.5 5.5" stroke="#ffffff" stroke-width="3.2" stroke-linecap="round"/>
      </svg>
    </div>
  </div>

  <section class="cocktail-list">
    <article class="cocktail-row">
      <div class="thumb bushwacker" role="img" aria-label="Photo of a creamy Bushwacker cocktail"></div>
      <h2 class="cocktail-name">151 Florida Bushwacker</h2>
      <div class="rating">
        <svg><use href="#star-full"/></svg><svg><use href="#star-full"/></svg><svg><use href="#star-half"/></svg><svg><use href="#star-empty"/></svg><svg><use href="#star-empty"/></svg>
      </div>
      <p class="have">You have: <span><b>4</b> of 8</span></p>
    </article>

    <article class="cocktail-row">
      <div class="thumb belmont" role="img" aria-label="Photo of a red Belmont cocktail"></div>
      <h2 class="cocktail-name">Belmont</h2>
      <div class="rating">
        <svg><use href="#star-full"/></svg><svg><use href="#star-empty"/></svg><svg><use href="#star-empty"/></svg><svg><use href="#star-empty"/></svg><svg><use href="#star-empty"/></svg>
      </div>
      <p class="have">You have: <span><b>7</b> of 8</span></p>
    </article>

    <article class="cocktail-row">
      <div class="thumb shade" role="img" aria-label="Photo of an In The Shade cocktail in a martini glass"></div>
      <h2 class="cocktail-name">In The Shade</h2>
      <div class="rating">
        <svg><use href="#star-full"/></svg><svg><use href="#star-full"/></svg><svg><use href="#star-full"/></svg><svg><use href="#star-full"/></svg><svg><use href="#star-empty"/></svg>
      </div>
      <p class="have complete">
        <svg width="30" height="30" viewBox="0 0 24 24" aria-label="Complete"><path d="M4 12.5l5 5L20 6" fill="none" stroke="var(--tick)" stroke-width="2.6" stroke-linecap="round" stroke-linejoin="round"/></svg>
        You have: <span class="total">8 of 8</span>
      </p>
    </article>

    <article class="cocktail-row">
      <div class="thumb bushwacker" role="img" aria-label="Photo of a creamy Bushwacker cocktail"></div>
      <h2 class="cocktail-name">151 Florida Bushwacker</h2>
      <div class="rating">
        <svg><use href="#star-full"/></svg><svg><use href="#star-full"/></svg><svg><use href="#star-half"/></svg><svg><use href="#star-empty"/></svg><svg><use href="#star-empty"/></svg>
      </div>
      <p class="have">You have: <span><b>4</b> of 8</span></p>
    </article>

    <article class="cocktail-row">
      <div class="thumb belmont" role="img" aria-label="Photo of a red Belmont cocktail"></div>
      <h2 class="cocktail-name">Belmont</h2>
      <div class="rating">
        <svg><use href="#star-full"/></svg><svg><use href="#star-empty"/></svg><svg><use href="#star-empty"/></svg><svg><use href="#star-empty"/></svg><svg><use href="#star-empty"/></svg>
      </div>
      <p class="have">You have: <span><b>7</b> of 8</span></p>
    </article>

    <article class="cocktail-row">
      <div class="thumb shade" role="img" aria-label="Photo of an In The Shade cocktail in a martini glass"></div>
      <h2 class="cocktail-name">In The Shade</h2>
    </article>

    <div class="list-fade"></div>
  </section>
</main>
</body>
</html>
```